Modern, clean and professional Wordpress design for a safety training company!

We are currently in the process of creating a new website for our business. We have hired a website developer and the main structure of our new Wordpress site is complete. We now need an overall design plan for the site. We need a very clean, professional and easy to follow website. Most of our website visitors only spend about 30-45 secs on our sites "shopping " so it is imperative that we have a strong Home Page.
Our company specializes in CPR and First Aid Certification Classes to businesses and individuals throughout Northern California. We provide these certifications two ways: ONSITE-We come to you, and HOSTED-we offer weekly classes at our 2 locations.
Our design needs to use the general green and blue colors of our logo. But we also like white.
The final design MUST communicate a legitimate, trustworthy and professional business. Our industry is VERY competitive and we need to STAND OUT.
Currently, the NEW website that we need a new design for is www.LifelineSkillsHub.com
Our old website is www.RescueCoursesBayview.com and we really do like the design of this website, but we just needed a Wordpress site for SEO purposes.
These are 3 websites that we really:
http://vorellamedica.com/
http://www.taldrix.com/
https://www.plumvey.com/
I have attached our Logo and other images if you need to use them but looking at the current two sites will be you best help.
Target Market(s)
1) Large businesses and industries that are looking for a company to provide ONSITE safety training classes at their office or place of work.
2) Individuals that need certifications for their jobs and other needs. These individuals are looking for a legitimate, trustworthy and professional environment to complete their training class.

```html
<!DOCTYPE html>
<html lang="en">
<head>
<meta charset="utf-8">
<title>Keystone Response Institute</title>
<link rel="stylesheet" href="https://fonts.googleapis.com/css2?family=Vollkorn:wght@400;600&family=Roboto+Slab:wght@300;400&display=swap">
<style>
:root{
  --blue:#213f97;
  --blue-dark:#16296a;
  --green:#8cc63f;
  --green-soft:#a4cf55;
  --grey:#ededed;
  --ink:#333;
  --footer:#2f2f2f;
}
*{box-sizing:border-box;margin:0;padding:0}
html,body{width:768px;height:1200px;overflow:hidden;background:var(--grey)}
body{position:relative;font-family:'Roboto Slab',serif;color:var(--ink)}
.abs{position:absolute}
.serif{font-family:'Vollkorn',serif}

.hero{left:0;top:0;width:768px;height:389px;background:linear-gradient(120deg,#6d6b6a 0%,#b9b4ad 35%,#d8d3cc 60%,#c4c0bb 100%)}
.hero-title{left:400px;top:212px;width:310px;font-family:'Vollkorn',serif;color:#3a3a3a;font-size:36px;line-height:40px;text-align:right}
.hero-title b{color:var(--blue);font-weight:600;font-size:46px}

.header{left:80px;top:0;width:608px;height:100px;background:#fff;border-radius:0 0 4px 4px;box-shadow:0 2px 6px rgba(0,0,0,.2)}
.brand{left:92px;top:26px;display:flex;align-items:center;gap:8px}
.brand-dot{width:18px;height:18px;border-radius:50%;background:var(--green)}
.brand-name{font-family:'Vollkorn',serif;color:var(--blue);font-size:17px;line-height:19px;width:140px}
.contact{right:90px;top:10px;text-align:right;font-family:'Vollkorn',serif;font-size:13px;line-height:21px;color:#333}
.contact svg{vertical-align:-2px;margin-right:4px}
.nav{left:264px;top:62px;width:428px;height:26px;background:var(--blue);display:flex;font-family:'Vollkorn',serif;font-size:10px}
.nav a{color:#fff;text-decoration:none;padding:0 9px;line-height:26px;white-space:nowrap}
.nav a.on{background:var(--green)}

.band{left:0;top:388px}
.card{width:128px;height:168px;top:426px;background:#fff;box-shadow:0 1px 4px rgba(0,0,0,.25);text-align:center}
.card h3{font-family:'Vollkorn',serif;font-weight:400;color:var(--blue);font-size:18px;line-height:18px;height:40px;display:flex;align-items:flex-end;justify-content:center;margin-top:22px}
.card .price{font-family:'Vollkorn',serif;color:var(--green);font-size:26px;margin:8px 0 4px}
.card p{font-size:9.5px;line-height:14px;font-family:'Vollkorn',serif;color:#222}
.card .btn{position:absolute;left:24px;bottom:-2px;width:80px;height:20px;background:var(--blue);color:#fff;font-family:'Vollkorn',serif;font-size:10px;line-height:18px;border-bottom:3px solid var(--blue-dark)}
.plus{display:inline-block;width:8px;height:8px;border-radius:50%;background:var(--green);vertical-align:-1px}

.rule{left:90px;top:628px;width:588px;height:1px;background:#d7d7d7}
.welcome{left:0;top:656px;width:768px;text-align:center;font-family:'Vollkorn',serif;font-size:20px;color:var(--blue)}
.welcome span{color:var(--green)}
.intro{left:100px;top:692px;width:568px;text-align:center;font-size:8.6px;line-height:13.5px;font-weight:300;color:#333}
.intro p+p{margin-top:12px}

.reviews-bg{left:0;top:810px;width:768px;height:239px;background:linear-gradient(90deg,#3c4f86,#2b3e78 50%,#3b4a7c)}
.review{left:96px;top:846px;width:270px;height:164px;background:rgba(255,255,255,.72);border-radius:3px;padding:10px 9px}
.review h4{font-family:'Vollkorn',serif;font-weight:400;font-size:19px;color:var(--blue)}
.stars{margin:6px 0 2px;display:flex;gap:3px}
.review .who{font-family:'Vollkorn',serif;font-size:10px;color:#333}
.review .who b{font-style:italic}
.review p{font-size:9px;line-height:13.5px;font-family:'Vollkorn',serif;color:#222;margin-top:2px}
.badge{left:232px;top:992px;width:60px;height:14px;background:#e6e6e6;border-radius:2px}
.arrows{left:298px;top:996px;width:52px;height:12px;background:#f3f3f3;border-radius:6px 6px 0 0}
.map{left:402px;top:848px;width:270px;height:162px;background:linear-gradient(135deg,#c9dcef 0%,#eae6d9 35%,#efe9dc 100%);outline:4px solid rgba(255,255,255,.25)}

.cta{left:90px;top:1061px;width:588px;height:59px;background:var(--green-soft);border-radius:3px;display:flex}
.cta div{flex:1;text-align:center;padding-top:8px}
.cta div+div{border-left:1px solid rgba(255,255,255,.5)}
.cta h5{font-family:'Vollkorn',serif;font-size:13px;color:var(--blue);font-weight:600}
.cta p{font-size:8.5px;line-height:13px;font-weight:300;color:#2a2a2a;padding:0 12px}

.footer{left:0;top:1133px;width:768px;height:67px;background:var(--footer)}
.links{left:92px;top:1150px;font-family:'Vollkorn',serif;font-size:8px;color:#fff}
.copy{left:92px;top:1174px;font-family:'Vollkorn',serif;font-size:8px;color:#fff}
.social{top:1167px;width:20px;height:20px;border-radius:50%;background:#2e6fb3;border:2px solid #fff}
.seal{left:647px;top:1142px;width:30px;height:48px;background:#fff;border-radius:2px}
</style>
</head>
<body>

<div class="abs hero" role="img" aria-label="Training room with an infant CPR manikin on a table"></div>
<h1 class="abs hero-title"><b>Leader</b> in CPR, BLS, and Basic First Aid Certifications</h1>

<header>
  <div class="abs header"></div>
  <div class="abs brand"><span class="brand-dot"></span><span class="brand-name">Keystone Response Institute</span></div>
  <div class="abs contact">
    <div><svg width="11" height="8" viewBox="0 0 11 8"><rect width="11" height="8" fill="#8cc63f"/><path d="M0 0l5.5 4.5L11 0" stroke="#fff" fill="none"/></svg>info@krirescue.com</div>
    <div><svg width="11" height="11" viewBox="0 0 24 24"><path fill="#8cc63f" d="M6.6 10.8c1.4 2.8 3.8 5.1 6.6 6.6l2.2-2.2c.3-.3.7-.4 1-.2 1.1.4 2.3.6 3.6.6.6 0 1 .4 1 1V20c0 .6-.4 1-1 1C10.6 21 3 13.4 3 4c0-.6.4-1 1-1h3.5c.6 0 1 .4 1 1 0 1.3.2 2.5.6 3.6.1.3 0 .7-.2 1z"/></svg>916-555-0172</div>
  </div>
  <nav class="abs nav"><a class="on">Home</a><a>About</a><a>Class Calender</a><a>Class For Groups</a><a>Certification Classes</a><a>Policies</a></nav>
</header>

<svg class="abs band" width="768" height="186" viewBox="0 0 768 186"><polygon points="0,0 768,0 768,100 0,184" fill="#213f97"/></svg>

<section>
  <div class="abs card" style="left:90px"><h3>CPR</h3><div class="price">$39</div><p>Adult/Child/Infant<br>90 Minutes!<br>No Book Fees! <span class="plus"></span></p><div class="btn">Register Now!</div></div>
  <div class="abs card" style="left:242px"><h3>BLS</h3><div class="price">$49</div><p>Adult/Child/Infant<br>90 Minutes!<br>No Book Fees!</p><div class="btn">Register Now!</div></div>
  <div class="abs card" style="left:396px"><h3>CPR<br>+First Aid</h3><div class="price">$59</div><p>Adult/Child/Infant<br>3 hours or less!<br>No Book Fees!</p><div class="btn">Register Now!</div></div>
  <div class="abs card" style="left:550px"><h3>BLS<br>+First Aid</h3><div class="price">$69</div><p>Adult/Child/Infant<br>3 hours or less!<br>No Book Fees! <span class="plus"></span></p><div class="btn">Register Now!</div></div>
</section>

<div class="abs rule"></div>
<h2 class="abs welcome serif"><span>Welcome to</span> Keystone Response Institute!</h2>
<div class="abs intro">
  <p>Keystone Response Institute is Northern California's leader in CPR, BLS, and Basic First Aid Certifications! Taught by experienced Firefighters, our classes are much shorter and provide common sense knowledge and skills to each student to help prepare them for actual emergencies.</p>
  <p>By using real life emergency responders, we have revolutionized the standard, boring CPR class by teaching students the need-to-know information and preparing them with facts and tips to help them in true life and death situations!</p>
</div>

<div class="abs reviews-bg" role="img" aria-label="Responders practising CPR on a manikin, tinted blue"></div>
<div class="abs review">
  <h4>People Reviews</h4>
  <div class="stars">
    <svg width="14" height="14" viewBox="0 0 24 24"><path fill="#f5b301" d="M12 2l3 7 7 .6-5.4 4.7 1.7 7.2L12 17.8 5.7 21.5l1.7-7.2L2 9.6 9 9z"/></svg>
    <svg width="14" height="14" viewBox="0 0 24 24"><path fill="#f5b301" d="M12 2l3 7 7 .6-5.4 4.7 1.7 7.2L12 17.8 5.7 21.5l1.7-7.2L2 9.6 9 9z"/></svg>
    <svg width="14" height="14" viewBox="0 0 24 24"><path fill="#f5b301" d="M12 2l3 7 7 .6-5.4 4.7 1.7 7.2L12 17.8 5.7 21.5l1.7-7.2L2 9.6 9 9z"/></svg>
    <svg width="14" height="14" viewBox="0 0 24 24"><path fill="#f5b301" d="M12 2l3 7 7 .6-5.4 4.7 1.7 7.2L12 17.8 5.7 21.5l1.7-7.2L2 9.6 9 9z"/></svg>
    <svg width="14" height="14" viewBox="0 0 24 24"><path fill="#f5b301" d="M12 2l3 7 7 .6-5.4 4.7 1.7 7.2L12 17.8 5.7 21.5l1.7-7.2L2 9.6 9 9z"/></svg>
  </div>
  <div class="who"><b>Danielle</b> - <i>CA, United States 25 Aug 2014</i></div>
  <p>Very informative and encouraging class! I learned that it is important for everyone to know how and why to perform CPR and I am so glad that I was able to learn the material from a firefighter who actually does this for a living.</p>
</div>
<div class="abs badge"></div>
<div class="abs arrows"></div>
<div class="abs map" role="img" aria-label="Road map of the Sacramento region with the training centre marked"></div>

<section class="abs cta">
  <div><h5>Register and Pay Online</h5><p>Registering/Paying Online will GUARANTEE your seat in class AND you will receive your certification the day of class!</p></div>
  <div><h5>Register Only and Pay Later</h5><p>Registering ONLY will NOT guarantee your seat in class and your certification will be mailed to you within 1-2 business days.</p></div>
</section>

<footer>
  <div class="abs footer"></div>
  <div class="abs links">Home &nbsp;|&nbsp; Class Calender &nbsp;|&nbsp; Certification Classes &nbsp;|&nbsp; Classes for Groups &nbsp;|&nbsp; About Us &nbsp;|&nbsp; Policies &nbsp;|&nbsp; Medesto &nbsp;|&nbsp; Manteca/Tracy &nbsp;|&nbsp; Livermore</div>
  <div class="abs copy">Copyright © 2015 Keystone Response Institute. All rights reserved.</div>
  <span class="abs social" style="left:346px"></span>
  <span class="abs social" style="left:380px"></span>
  <span class="abs social" style="left:414px"></span>
  <div class="abs seal"></div>
</footer>

</body>
</html>
```